Clean professional design needed for landscape property business

We need a logo for a new lawncare, landscaping , property maintenance business called Meadow Trim.
Our services include lawn mowing, garden maintenance, clean ups and some property maintenance.
We want a double sided business card that is clean and very professional using the colour scheme from our logo which is provided.
the business card should have impact as we will use these to drop into people's letterboxes as a marketing drop.
Initially we want to see what you come up with so there is a very wide scope here to work with.
Updates

Project Deadline Extended
Reason: we feel our original deadline was too short. we have extended to give more time for quality submissions.

Target Market(s)

High end property owners who don't wish to do there own gardneing or property maintenance

Industry/Entity Type

Business

Contact Information for Business Card

Name
Postion/ Title
Phone number
mobile
web address
physical address

services offered

Font styles to use
Sans Serif

Requirements
Must have
• curved edges preferrred
Nice to have
• We like the idea of the logo being embossed or etched into the card so it looks like it is below the surface of the card
Should not have
• No stock images or characters.

```html
<!DOCTYPE html>
<html lang="en">
<head>
<meta charset="utf-8">
<title>Meadow Trim – Business Card</title>
<link href="https://fonts.googleapis.com/css2?family=Arimo:wght@400;700&display=swap" rel="stylesheet">
<style>
  :root {
    --page-bg: #e6e7e8;
    --card-white: #ffffff;
    --card-grey: #59595b;
    --ink: #4d4d4f;
    --ink-soft: #58595b;
    --leaf-green: #7dbb42;
    --logo-on-dark: #6e6e70;
  }
  * { margin: 0; padding: 0; box-sizing: border-box; }
  html, body { width: 1200px; height: 1200px; overflow: hidden; }
  body {
    background: var(--page-bg);
    font-family: "Arimo", Arial, sans-serif;
    color: var(--ink);
    position: relative;
  }
  .card {
    position: absolute;
    top: 448px;
    width: 522px;
    height: 298px;
  }
  .card-front {
    left: 46px;
    background: var(--card-white);
    border-radius: 0 22px 22px 0;
  }
  .card-back {
    left: 621px;
    background: var(--card-grey);
    border-radius: 0 22px 22px 22px;
  }
  .person-name {
    position: absolute; left: 26px; top: 50px;
    font-size: 21px; color: var(--leaf-green); letter-spacing: 0.2px;
  }
  .person-title {
    position: absolute; left: 26px; top: 76px;
    font-size: 13px; color: var(--ink-soft);
  }
  .brand-name {
    position: absolute;
    font-weight: 700;
    letter-spacing: -1.5px;
    line-height: 1;
    white-space: nowrap;
  }
  .card-front .brand-name { left: 252px; top: 52px; font-size: 37px; color: var(--ink); }
  .brand-square {
    position: absolute; background: var(--leaf-green);
  }
  .card-front .brand-square { left: 462px; top: 58px; width: 13px; height: 13px; }
  .contact-list {
    position: absolute; left: 26px; top: 137px;
    list-style: none; font-size: 13px; color: var(--ink-soft);
  }
  .contact-list li { display: flex; align-items: center; height: 21px; }
  .contact-list svg { width: 10px; height: 10px; margin-right: 7px; fill: var(--leaf-green); }
  .address {
    position: absolute; left: 26px; top: 236px;
    font-size: 13px; line-height: 17px; color: var(--ink-soft);
  }
  .address-rule {
    position: absolute; left: 166px; top: 264px;
    width: 341px; height: 2px; background: var(--leaf-green);
  }
  .card-back .brand-name { left: 108px; top: 128px; font-size: 42px; color: var(--logo-on-dark); }
  .card-back .brand-square { left: 362px; top: 134px; width: 15px; height: 15px; }
  .services-band {
    position: absolute; left: 0; right: 0; top: 264px;
    display: flex; align-items: center; justify-content: space-between;
  }
  .band-tab { width: 15px; height: 10px; background: var(--leaf-green); }
  .services {
    font-size: 11px; font-weight: 700; color: #fff; letter-spacing: 0.1px;
    white-space: nowrap;
  }
  .services .sep { color: var(--leaf-green); padding: 0 3px; }
</style>
</head>
<body>
  <section class="card card-front" aria-label="Business card front">
    <div class="person-name">Jordan Hale</div>
    <div class="person-title">Chief Executive Officer</div>
    <div class="brand-name">meadowtrim</div>
    <div class="brand-square"></div>
    <ul class="contact-list">
      <li><svg viewBox="0 0 10 10" aria-hidden="true"><path d="M2 0.5 L3.6 2.6 L2.8 3.7 Q3.6 5.8 6.3 7.2 L7.4 6.4 L9.5 8 L8.2 9.5 Q1.5 8 0.5 1.8 Z"/></svg>555-014-2231</li>
      <li><svg viewBox="0 0 10 10" aria-hidden="true"><path d="M2.5 0 H7.5 V10 H2.5 Z M3.5 1 V8 H6.5 V1 Z"/></svg>555-017-6408</li>
      <li><svg viewBox="0 0 10 10" aria-hidden="true"><path d="M5 0 A5 5 0 1 0 5.01 0 Z M5 1 A4 4 0 0 1 8.9 4.5 H1.1 A4 4 0 0 1 5 1 Z M1.1 5.5 H8.9 A4 4 0 0 1 1.1 5.5 Z"/></svg>www.meadowtrim.com</li>
    </ul>
    <div class="address">410 Orchard Lane<br>Suite 120, VA 20100</div>
    <div class="address-rule"></div>
  </section>

  <section class="card card-back" aria-label="Business card back">
    <div class="brand-name">meadowtrim</div>
    <div class="brand-square"></div>
    <div class="services-band">
      <span class="band-tab"></span>
      <p class="services">LAWN MOWING<span class="sep">|</span>GARDEN MAINTENANCE<span class="sep">|</span>CLEAN UPS &amp; SOME PROPERTY MAINTENANCE</p>
      <span class="band-tab"></span>
    </div>
  </section>
</body>
</html>
```